Marrowgate Auctions Business Cards Design Needed

I need a business card design that is modern looking - double sided (maybe just my logo on the back, but open to suggestions) - the overall design is up to you. I want it to be easy to read - not over the top flashy. I already have a company logo which I uploaded so that needs to be used. The colors of my logo are the colors I want on the card... so blue and gray (do need to match the logo colors).

Requirements
Must have
• Would like the card to be sleek, modern and easy to ready

```html
<!DOCTYPE html>
<html lang="en">
<head>
<meta charset="utf-8">
<title>Marrowgate Auctions – Business Cards</title>
<link rel="stylesheet" href="https://fonts.googleapis.com/css2?family=Roboto:wght@400;700&display=swap">
<style>
  :root {
    --page-bg: #ebeced;
    --card-bg: #070808;
    --brand-blue: #2e86ee;
    --brand-gray: #4a5359;
    --text-gray: #5f6469;
  }
  html, body {
    margin: 0;
    padding: 0;
    width: 1200px;
    height: 1200px;
    overflow: hidden;
    background: var(--page-bg);
    font-family: "Roboto", Arial, sans-serif;
  }
  .canvas {
    position: relative;
    width: 1200px;
    height: 1200px;
  }
  .card {
    position: absolute;
    background: var(--card-bg);
    border-radius: 36px;
    overflow: hidden;
  }
  .card--front { left: 123px; top: 37px; width: 954px; height: 545px; }
  .card--back  { left: 122px; top: 621px; width: 956px; height: 547px; }

  .brand-square {
    position: absolute;
    left: 50%;
    width: 140px;
    height: 140px;
    margin-left: -70px;
    background: var(--brand-blue);
  }
  .card--front .brand-square { top: 58px; }
  .card--back .brand-square  { top: 106px; }

  .brand-name {
    position: absolute;
    left: 0;
    right: 0;
    margin: 0;
    text-align: center;
    font-weight: 700;
    font-size: 58px;
    letter-spacing: 1px;
    text-transform: uppercase;
    color: var(--brand-gray);
    line-height: 1;
  }
  .card--front .brand-name { top: 258px; }
  .card--back .brand-name  { top: 306px; }

  .person-name {
    position: absolute;
    top: 340px;
    left: 0;
    right: 0;
    margin: 0;
    text-align: center;
    font-weight: 400;
    font-size: 40px;
    letter-spacing: 1px;
    color: var(--brand-blue);
    line-height: 1;
  }
  .person-title {
    position: absolute;
    top: 386px;
    left: 0;
    right: 0;
    margin: 0;
    text-align: center;
    font-size: 28px;
    letter-spacing: 1.5px;
    color: var(--text-gray);
    line-height: 1;
  }
  .contact-list {
    position: absolute;
    top: 426px;
    left: 322px;
    margin: 0;
    padding: 0;
    list-style: none;
  }
  .contact-item {
    display: flex;
    align-items: center;
    height: 29px;
    font-size: 25px;
    letter-spacing: 1px;
    color: var(--text-gray);
  }
  .contact-icon {
    width: 20px;
    height: 20px;
    margin-right: 10px;
    fill: none;
    stroke: var(--brand-blue);
    stroke-width: 2;
  }
  .tagline {
    position: absolute;
    top: 404px;
    left: 0;
    right: 0;
    margin: 0;
    text-align: center;
    font-size: 38px;
    letter-spacing: 1.5px;
    color: var(--text-gray);
    line-height: 1;
  }
  .tagline__accent { color: var(--brand-blue); }
</style>
</head>
<body>
<main class="canvas">
  <section class="card card--front" aria-label="Card front">
    <div class="brand-square"></div>
    <h1 class="brand-name">Marrowgate Auctions</h1>
    <p class="person-name">Dana Whitlow</p>
    <p class="person-title">Owner/President - Auctioneer</p>
    <ul class="contact-list">
      <li class="contact-item">
        <svg class="contact-icon" viewBox="0 0 20 20" aria-hidden="true">
          <path d="M4 2 L7.5 2 L8.5 6.5 L6.5 8 Q8 12 12 13.5 L13.5 11.5 L18 12.5 L18 16 Q17 18 14.5 18 Q3 16 2 5.5 Q2 3 4 2 Z" fill="var(--brand-blue)" stroke="none"/>
        </svg>
        702-555-0148
      </li>
      <li class="contact-item">
        <svg class="contact-icon" viewBox="0 0 20 20" aria-hidden="true">
          <rect x="1.5" y="4" width="17" height="12" fill="var(--brand-blue)" stroke="none"/>
          <path d="M1.5 4 L10 11 L18.5 4 M1.5 16 L7.5 9.5 M18.5 16 L12.5 9.5" stroke="var(--card-bg)" stroke-width="1.5"/>
        </svg>
        hello@marrowgateauctions.com
      </li>
      <li class="contact-item">
        <svg class="contact-icon" viewBox="0 0 20 20" aria-hidden="true">
          <circle cx="10" cy="10" r="8"/>
          <ellipse cx="10" cy="10" rx="3.5" ry="8"/>
          <path d="M2 10 H18 M3.5 6 H16.5 M3.5 14 H16.5"/>
        </svg>
        bidrevival.com
      </li>
    </ul>
  </section>

  <section class="card card--back" aria-label="Card back">
    <div class="brand-square"></div>
    <h2 class="brand-name">Marrowgate Auctions</h2>
    <p class="tagline"><span class="tagline__accent">Improving Charity</span> Auctions Nationwide</p>
  </section>
</main>
</body>
</html>
```